Business Card Design Project

Design business card based on logo provided.

Industry/Entity Type

Business

Requirements
Nice to have
• Logo to be provided.

Solid green second side with reverse logo (buildings only, not text).

Because the logo is linear I think that it might be possible to extend the logo lines across the card (only on the second side) as an interesting design element.

"Helping Owners Build Better Building Programs"

"Job Order Contracting and Best Value Specialist"

"Cooperation - Innovation - Efficiency"

Basic Info:
Nora Whitfield
Owner/Founder
505-718-6024
nora@norawhitfieldpartners.example

www.norawhitfieldpartners.example (this should probably be on reverse)

```html
<!DOCTYPE html>
<html lang="en">
<head>
<meta charset="utf-8">
<title>Nora Whitfield Partners – Business Card</title>
<link href="https://fonts.googleapis.com/css2?family=Arimo:wght@400;700&display=swap" rel="stylesheet">
<style>
  :root {
    --page-bg: #ffffff;
    --brand-green: #a5bf3f;
    --brand-green-deep: #9fba38;
    --card-fade: #f4f6ec;
    --card-base: #e4e4e2;
    --ink-white: #ffffff;
    --ink-grey: #4a4a48;
    --ink-logo: #5a5a57;
    --ink-mark: #6f8a2a;
    --ink-notes: #111111;
  }
  * { box-sizing: border-box; margin: 0; padding: 0; }
  html, body {
    width: 1200px;
    height: 900px;
    overflow: hidden;
    background: var(--page-bg);
    font-family: "Arimo", Arial, sans-serif;
  }
  .sheet {
    position: relative;
    width: 1200px;
    height: 900px;
  }
  .card {
    position: absolute;
    top: 224px;
    width: 520px;
    height: 338px;
  }
  .card--front {
    left: 46px;
    background: linear-gradient(180deg,
      var(--brand-green) 0%,
      #c3d584 28%,
      var(--card-fade) 55%,
      #eeeeec 78%,
      var(--card-base) 100%);
  }
  .card--back {
    left: 632px;
    background: var(--brand-green-deep);
  }
  .contact {
    position: absolute;
    left: 34px;
    top: 20px;
    color: var(--ink-white);
  }
  .contact__name {
    font-size: 17px;
    font-weight: 700;
    line-height: 22px;
  }
  .contact__line {
    font-size: 13px;
    line-height: 16px;
  }
  .taglines {
    position: absolute;
    top: 140px;
    color: var(--ink-grey);
    font-size: 13px;
  }
  .taglines__line {
    position: absolute;
    white-space: nowrap;
  }
  .taglines__line--1 { left: 160px; top: 0; }
  .taglines__line--2 { left: 170px; top: 26px; }
  .taglines__line--3 { left: 182px; top: 51px; }
  .wordmark {
    position: absolute;
    left: 34px;
    top: 230px;
    display: flex;
    align-items: center;
    gap: 16px;
  }
  .wordmark__square {
    width: 70px;
    height: 70px;
    background: var(--ink-mark);
  }
  .wordmark__name {
    color: var(--ink-logo);
    font-size: 26px;
    font-weight: 400;
    letter-spacing: 0.5px;
    text-transform: uppercase;
    white-space: nowrap;
  }
  .back-name {
    position: absolute;
    left: 0;
    right: 0;
    top: 120px;
    text-align: center;
    color: var(--ink-white);
    font-size: 36px;
    font-weight: 400;
    letter-spacing: 1px;
    text-transform: uppercase;
  }
  .back-url {
    position: absolute;
    left: 0;
    right: 0;
    top: 278px;
    text-align: center;
    color: var(--ink-white);
    font-size: 16px;
  }
  .specs {
    position: absolute;
    left: 412px;
    top: 650px;
    color: var(--ink-notes);
    font-size: 16px;
  }
  .specs__title { margin-bottom: 40px; }
  .specs__size { word-spacing: 2px; }
  .specs__gap { display: inline-block; width: 12px; }
</style>
</head>
<body>
<main class="sheet">
  <section class="card card--front" aria-label="Business card front">
    <div class="contact">
      <p class="contact__name">Nora Whitfield</p>
      <p class="contact__line">Owner/Founder</p>
      <p class="contact__line">505-718-6024</p>
      <p class="contact__line">nora@norawhitfieldpartners.example</p>
    </div>
    <div class="taglines">
      <p class="taglines__line taglines__line--1">Helping Owners Build Better Building Programs</p>
      <p class="taglines__line taglines__line--2">Job Order Contracting and Best Value Specialist</p>
      <p class="taglines__line taglines__line--3">Cooperation - Innovation - Efficiency</p>
    </div>
    <div class="wordmark">
      <span class="wordmark__square" aria-hidden="true"></span>
      <span class="wordmark__name">Nora Whitfield Partners</span>
    </div>
  </section>

  <section class="card card--back" aria-label="Business card back">
    <p class="back-name">Nora Whitfield Partners</p>
    <p class="back-url">www.norawhitfieldpartners.example</p>
  </section>

  <aside class="specs">
    <p class="specs__title">Business card details:</p>
    <p class="specs__size">Card size: <span class="specs__gap"></span>92mm x 60mm <span class="specs__gap"></span>3mm bleed</p>
  </aside>
</main>
</body>
</html>
```